KORVALD GmbH

We need an improvement of the existing design of our webpage (www.korvald.de).
We are a Munich based IT services company offering application consulting, system infrastructure consulting and outsourcing. We do not want to completely restructure our website, instead we want to have an improvement of the existing one. So the design should fit into the already existing page enhance or modify it and make it look more professional. For example the slideshow could be improved with pictures that better fit. Furthermore the logo could also be improved and modified. Also the tables, and layers could be improved. As a result we do not expect radical changes but rather a more clean and improved look compared to the as-is situation. The design should communicate professionalism, experience and success.

Target Market(s)

small and medium sized companies.

Requirements
Must have
• Logo improvement, slideshow improvement, table and layer improvement
Should not have
• Only care about the landing page.

```html
<!DOCTYPE html>
<html lang="en">
<head>
<meta charset="utf-8">
<title>KORVALD GmbH – IT-Dienstleistungen</title>
<link href="https://fonts.googleapis.com/css2?family=Source+Sans+3:wght@400;600;700&display=swap" rel="stylesheet">
<style>
:root{
  --brand:#0a4fa3;
  --brand-light:#1b6fc9;
  --text:#555;
  --muted:#7a7a7a;
  --rule:#d8d8d8;
  --nav-top:#2b2b2b;
  --nav-bottom:#0f0f0f;
  --footer:#2a2a2a;
  --white:#fff;
}
*{margin:0;padding:0;box-sizing:border-box}
html,body{width:1200px;height:1200px;overflow:hidden;background:var(--white);font-family:"Source Sans 3",Arial,sans-serif;color:var(--text)}
.page{position:relative;width:1200px;height:1200px}
.header{position:absolute;top:0;left:0;width:1200px;height:117px;background:linear-gradient(#fff,#f3f3f3);border-bottom:1px solid #ccc}
.brand{position:absolute;left:100px;top:22px}
.brand-name{font-size:44px;font-weight:700;color:var(--brand);letter-spacing:.5px;line-height:1}
.brand-tagline{font-size:18px;color:var(--brand);margin-top:6px}
.call{position:absolute;right:99px;top:42px;font-size:23px;color:#8a8a8a;display:flex;align-items:center;gap:10px}
.call strong{font-weight:400;color:var(--brand)}
.nav{position:absolute;top:117px;left:0;width:1200px;height:53px;background:linear-gradient(var(--nav-top),var(--nav-bottom))}
.nav ul{list-style:none;display:flex;position:absolute;left:104px;top:13px}
.nav li{font-size:15px;color:var(--white);padding:3px 27px;border-right:1px solid #555;line-height:22px}
.nav li:first-child{padding-left:26px;color:#6db7ff}
.search{position:absolute;right:99px;top:11px;width:242px;height:31px;background:var(--white);font-size:14px;color:#333;padding:6px 18px;display:flex;justify-content:space-between;align-items:center}
.hero{position:absolute;top:170px;left:0;width:1200px;height:398px;background:radial-gradient(ellipse at 62% 45%,#6fb4f0 0%,#2a7bd3 35%,#0d4fae 75%,#0a3f94 100%)}
.hero h1{position:absolute;left:101px;top:115px;width:360px;font-size:29px;font-weight:600;line-height:41px;color:var(--white);text-shadow:0 2px 3px rgba(0,0,0,.4)}
.hero .next{position:absolute;left:1057px;top:176px}
.features{position:absolute;top:598px;left:100px;width:1001px;display:flex;justify-content:space-between}
.feature{width:336px;text-align:center}
.feature svg{height:66px;display:block;margin:0 auto}
.feature h2{font-size:26px;font-weight:400;color:var(--brand);margin-top:12px}
.feature p{font-size:14.5px;line-height:23px;color:var(--muted);margin-top:6px;padding:0 24px}
.rule{position:absolute;left:100px;width:1001px;height:1px;background:var(--rule)}
.welcome h2{position:absolute;left:111px;top:833px;font-size:26px;font-weight:400;color:var(--brand)}
.welcome p{position:absolute;left:111px;top:878px;width:697px;font-size:15px;line-height:25px;color:var(--text)}
.welcome .photo{position:absolute;left:839px;top:839px;width:252px;height:131px;border:1px solid #ccc;background:linear-gradient(90deg,#d9dde2,#eef0f2 50%,#c9ced6)}
.partners{position:absolute;top:1028px;left:0;width:1200px;height:70px}
.badge{position:absolute}
.footer{position:absolute;top:1118px;left:0;width:1200px;height:82px;background:var(--footer)}
.footer-nav{position:absolute;left:100px;top:32px;display:flex;align-items:center;font-size:14px;color:#bbb}
.footer-nav span.sep{margin:0 9px;color:#888}
.social{display:flex;gap:9px;margin-left:16px}
.social i{width:25px;height:25px;border-radius:50%;background:#666;display:block}
.copy{position:absolute;right:99px;top:34px;font-size:14px;color:#bbb}
</style>
</head>
<body>
<div class="page">
  <header class="header">
    <div class="brand">
      <div class="brand-name">KORVALD GmbH</div>
      <div class="brand-tagline">IT-Dienstleistungen für Ihr Unternehmen</div>
    </div>
    <div class="call">
      <svg width="22" height="20" viewBox="0 0 22 20"><path d="M4 2c2-1 3 0 4 2l1 2c0 1-1 2-2 2 1 3 3 5 6 6 0-1 1-2 2-2l2 1c2 1 3 2 2 4-1 2-3 3-6 2C7 17 3 12 2 7 1 5 2 3 4 2z" fill="#999"/></svg>
      <span>Call us : <strong>+49891234500</strong></span>
    </div>
  </header>

  <nav class="nav">
    <ul>
      <li>HOME</li><li>ABOUT US</li><li>OUR SERVICES</li><li>CONTACT US</li>
    </ul>
    <div class="search">Search
      <svg width="16" height="16" viewBox="0 0 16 16"><circle cx="6" cy="6" r="4.5" fill="none" stroke="#222" stroke-width="2.5"/><line x1="9.5" y1="9.5" x2="14.5" y2="14.5" stroke="#222" stroke-width="3" stroke-linecap="round"/></svg>
    </div>
  </nav>

  <section class="hero" role="img" aria-label="Businesswoman touching a futuristic blue interface with world map, charts and data panels">
    <h1>We are IT service provider specializing in the needs of small and medium-sized enterprises</h1>
    <svg class="next" width="42" height="42" viewBox="0 0 42 42"><circle cx="21" cy="21" r="20" fill="rgba(255,255,255,.55)" stroke="#fff" stroke-width="1.5"/><path d="M18 13l8 8-8 8" fill="none" stroke="#666" stroke-width="2"/></svg>
  </section>

  <section class="features">
    <div class="feature">
      <svg viewBox="0 0 66 66" width="66">
        <g fill="var(--brand)">
          <circle cx="33" cy="33" r="23"/>
          <g transform="translate(33 33)">
            <rect x="-6" y="-33" width="12" height="14"/><rect x="-6" y="19" width="12" height="14"/>
            <rect x="-33" y="-6" width="14" height="12"/><rect x="19" y="-6" width="14" height="12"/>
            <g transform="rotate(45)"><rect x="-6" y="-33" width="12" height="14"/><rect x="-6" y="19" width="12" height="14"/><rect x="-33" y="-6" width="14" height="12"/><rect x="19" y="-6" width="14" height="12"/></g>
          </g>
        </g>
        <circle cx="33" cy="33" r="12" fill="#fff"/><circle cx="33" cy="33" r="7" fill="var(--brand)"/>
      </svg>
      <h2>Application support</h2>
      <p>Class aptent taciti sociosqu ad litora torquent per conubia nostra, per inceptos himenaeos facilisis lacus.</p>
    </div>
    <div class="feature">
      <svg viewBox="0 0 80 66" width="80">
        <rect x="3" y="3" width="74" height="48" fill="none" stroke="var(--brand)" stroke-width="6"/>
        <rect x="8" y="8" width="64" height="38" fill="var(--brand-light)"/>
        <rect x="34" y="54" width="12" height="6" fill="var(--brand)"/><rect x="24" y="60" width="32" height="4" fill="var(--brand)"/>
      </svg>
      <h2>System Support</h2>
      <p>Class aptent taciti sociosqu ad litora torquent per conubia nostra, per inceptos himenaeos facilisis lacus.</p>
    </div>
    <div class="feature">
      <svg viewBox="0 0 66 66" width="66">
        <line x1="8" y1="8" x2="56" y2="58" stroke="var(--brand)" stroke-width="8" stroke-linecap="round"/>
        <line x1="54" y1="10" x2="10" y2="56" stroke="var(--brand)" stroke-width="8" stroke-linecap="round"/>
        <circle cx="54" cy="10" r="9" fill="none" stroke="var(--brand)" stroke-width="5"/>
      </svg>
      <h2>Holistic care</h2>
      <p>Class aptent taciti sociosqu ad litora torquent per conubia nostra, per inceptos himenaeos facilisis lacus.</p>
    </div>
  </section>

  <div class="rule" style="top:809px"></div>

  <section class="welcome">
    <h2>Welcome to KORVALD GmbH</h2>
    <p>Duis enim tellus, venenatis ac volutpat vel, viverra in sapien. Proin a mi eu nisl facilisis ultricies a id nunc. Nunc vehicula erat quis nulla placerat viverra. Quisque vel imperdiet nisi. Nunc tortor lectus, vehicula quis pretium at, ultrices vitae nunc. Sed augue turpis, sodales eu nisl nec, tincidunt rutrum nulla. Nunc commodo lectus faucibus, interdum dolor sit amet, semper ante.</p>
    <div class="photo" role="img" aria-label="Smiling businesswoman in an office with colleagues working at a laptop behind her"></div>
  </section>

  <div class="rule" style="top:1003px"></div>

  <section class="partners" aria-label="Partner badges">
    <div class="badge" style="left:153px;top:3px;width:136px;height:65px;border-radius:5px;background:linear-gradient(#6f9fd6,#3d74b8)"></div>
    <div class="badge" style="left:369px;top:3px;width:143px;height:65px;background:#1a9ad9"></div>
    <div class="badge" style="left:600px;top:3px;width:295px;height:65px;background:#1c1c1c"></div>
    <div class="badge" style="left:982px;top:2px;width:65px;height:66px;background:#66c400"></div>
  </section>

  <footer class="footer">
    <div class="footer-nav">
      <span>Home</span><span class="sep">|</span><span>About us</span><span class="sep">|</span><span>Our Services</span><span class="sep">|</span><span>Contact us</span>
      <div class="social"><i></i><i></i></div>
    </div>
    <div class="copy">Copyright © 2013 &nbsp; Korvald. &nbsp; All rights reserved</div>
  </footer>
</div>
</body>
</html>
```